Single Side Postcard Size Flyer Design

We want to design an attractive and eye-catching sign for hair stylists and barbers to sit on their workstations to attract the attention of their clients regarding hair loss and encourage them to speak to their stylist about it of they are would like to seek treatment.
Many men and women suffer from hair loss, but are often in denial it is happening or too embarrassed to talk about it.
This postcard sized flyer is designed to stick to the mirror at their hair stylist or barber and encourage them to ask their stylist about it.
We want this to be very plain and simple. With just perhaps some kind of simple head line and worry lines. I have uploaded a simple idea.
I have also uploaded the print templates that must be used to provide final designs.

Target Market(s)

Men aged 25 to 60 with thinning hair

Industry/Entity Type

Healthcare

Font styles to use
Sans Serif

Colors
0355a3
ffffff
cfcfcf
1b1b1b

Requirements
Must have
• Flyer size is vertical 4" x 6"
• Copy for the flyer is as follows ans is in color blue: #014ca5
• Worried About Thinning Hair?
• 2 out of 3 Men will have visible hair loss by age 35.
• The Good News is that your
• Barber or Stylist can tell you how to
• stop the loss & grow back your hair.
• Just ask.
• The Brisk Lattice Program from
• The Marlow Pine Company
• New Science. No Surgery. Your Hair.
• www.quellvantinfo.example
Should not have
• - dont add any logos, images or ornate design. this needs to be simple, easy to ready and eye catching.
• - do not use the color red in any capacity.

```html
<!DOCTYPE html>
<html lang="en">
<head>
<meta charset="utf-8">
<title>Worried About Thinning Hair? – The Marlow Pine Company</title>
<link rel="stylesheet" href="https://fonts.googleapis.com/css2?family=Arvo:wght@400;700&family=Open+Sans:wght@400;700&display=swap">
<style>
  :root {
    --backdrop: #4e4e4e;
    --card: #e7e8ea;
    --brand-blue: #0b56a4;
    --band-blue: #0c55a0;
    --ink-gray: #5a5a5a;
    --frame-gray: #6a6a6a;
    --white: #ffffff;
  }
  html, body {
    margin: 0;
    width: 960px;
    height: 1200px;
    overflow: hidden;
    background: var(--backdrop);
  }
  .flyer {
    position: absolute;
    left: 80px;
    top: 0;
    width: 800px;
    height: 1200px;
    background: var(--card);
    text-align: center;
    overflow: hidden;
  }
  .flyer > * { position: absolute; left: 0; right: 0; margin: 0; line-height: 1; }
  .slab { font-family: "Arvo", "Rockwell", serif; }
  .sans { font-family: "Open Sans", sans-serif; }

  .headline {
    top: 78px;
    color: var(--brand-blue);
    font-weight: 400;
    font-size: 80px;
    line-height: 76px;
    letter-spacing: 0.5px;
  }
  .stat {
    top: 251px;
    color: var(--ink-gray);
    font-size: 27px;
  }
  .stat strong { font-weight: 700; }

  .news-box {
    left: 39px;
    right: 40px;
    top: 356px;
    height: 231px;
    border: 2px solid var(--frame-gray);
  }
  .news-shadow {
    top: 589px;
    left: 60px;
    right: 60px;
    height: 80px;
    background: radial-gradient(ellipse 50% 55% at 50% 0%, rgba(0,0,0,0.55), rgba(0,0,0,0.12) 55%, rgba(0,0,0,0) 100%);
  }
  .news-lead {
    top: 393px;
    color: var(--brand-blue);
    font-size: 50px;
    line-height: 45px;
  }
  .news-body {
    top: 488px;
    color: var(--ink-gray);
    font-size: 30px;
    line-height: 36px;
  }

  .cta {
    top: 672px;
    color: var(--brand-blue);
    font-size: 78px;
  }
  .program {
    top: 760px;
    color: var(--ink-gray);
    font-size: 31px;
  }
  .web {
    top: 800px;
    color: var(--ink-gray);
    font-size: 43px;
  }

  .brand-band {
    top: 936px;
    height: 264px;
    background: var(--band-blue);
  }
  .company {
    top: 1021px;
    color: var(--white);
    font-weight: 700;
    font-size: 45px;
  }
  .tagline {
    top: 1072px;
    color: var(--white);
    font-size: 35px;
  }
</style>
</head>
<body>
  <main class="flyer">
    <h1 class="headline slab">WORRIED ABOUT<br>THINNING HAIR?</h1>
    <p class="stat sans">2 out of 3 Men will have visible hair loss by <strong>AGE 35.</strong></p>

    <div class="news-shadow" aria-hidden="true"></div>
    <div class="news-box" aria-hidden="true"></div>
    <h2 class="news-lead slab">THE GOOD NEWS<br>IS THAT YOUR</h2>
    <p class="news-body sans">BARBER OR STYLIST CAN TELL YOU HOW TO<br>STOP THE LOSS &amp; GROW BACK YOUR HAIR.</p>

    <h2 class="cta slab">JUST ASK.</h2>
    <p class="program slab">THE BRISK LATTICE PROGRAM FROM</p>
    <p class="web slab">www.quellvantinfo.example</p>

    <div class="brand-band" aria-hidden="true"></div>
    <p class="company slab">THE MARLOW PINE COMPANY</p>
    <p class="tagline sans">New Science. No Surgery. Your Hair.</p>
  </main>
</body>
</html>
```